Accounting services

Looking for a Business card & Logo design

company name - LUMEN ACCOUNTING & TAXATION SOLUTIONS

name - Corwin Pell

position - Accountant / Business Consultant

email - "undecided"

Tel : (868) 512-4873 / (868) 587-2196

**PUT THESE TO THE BACK**
Accounting - VAT * INCOME/CORP TAX * RETURNS

REGISTRATION - VAT * NIS * Company Registration/Business Plan

Industry/Entity Type

Business

```html
<!DOCTYPE html>
<html lang="en">
<head>
<meta charset="utf-8">
<title>Lumen Accounting &amp; Taxation Solutions – Business Card</title>
<link rel="stylesheet" href="https://fonts.googleapis.com/css2?family=Noto+Sans:wght@400;700&family=Open+Sans:wght@400&family=Archivo+Black&display=swap">
<style>
  :root {
    --sky-top: #5fb2cf;
    --sky-mid: #a9d6e6;
    --paper: #ffffff;
    --paper-foot: #e9f3f8;
    --band: #4b8497;
    --band-text: #ffffff;
    --role-text: #4a5566;
    --contact-text: #0a0a0a;
    --mark-ring: #dfe7ee;
    --mark-text: #3d7fb8;
  }
  html, body {
    margin: 0;
    padding: 0;
    overflow: hidden;
    background: #ffffff;
  }
  .card {
    position: relative;
    width: 1200px;
    height: 686px;
    overflow: hidden;
    background: linear-gradient(to bottom,
      var(--sky-top) 0%,
      var(--sky-mid) 22%,
      var(--paper) 52%,
      var(--paper) 78%,
      var(--paper-foot) 100%);
    font-family: "Noto Sans", sans-serif;
  }
  .brand-mark {
    position: absolute;
    left: 36px;
    top: 126px;
    width: 160px;
    height: 160px;
    border-radius: 50%;
    background: var(--paper);
    border: 4px solid var(--mark-ring);
    box-sizing: border-box;
    display: flex;
    align-items: center;
    justify-content: center;
  }
  .brand-mark__name {
    font-family: "Noto Sans", sans-serif;
    font-weight: 700;
    font-size: 28px;
    letter-spacing: 2px;
    color: var(--mark-text);
  }
  .title-band {
    position: absolute;
    left: 245px;
    top: 110px;
    width: 762px;
    height: 199px;
    background: var(--band);
  }
  .company-name {
    position: absolute;
    left: 263px;
    top: 116px;
    margin: 0;
    font-family: "Noto Sans", sans-serif;
    font-weight: 400;
    font-size: 48px;
    line-height: 66px;
    letter-spacing: 9px;
    color: var(--band-text);
    white-space: nowrap;
  }
  .person-name {
    position: absolute;
    left: 265px;
    top: 252px;
    margin: 0;
    font-family: "Noto Sans", sans-serif;
    font-weight: 700;
    font-size: 34px;
    color: var(--band-text);
  }
  .role {
    position: absolute;
    left: 388px;
    top: 324px;
    margin: 0;
    font-family: "Open Sans", sans-serif;
    font-size: 35px;
    color: var(--role-text);
  }
  .contact {
    position: absolute;
    left: 28px;
    top: 556px;
    margin: 0;
    font-family: "Archivo Black", sans-serif;
    font-size: 29px;
    line-height: 40px;
    letter-spacing: -1px;
    color: var(--contact-text);
    text-shadow: 0 0 3px #ffffff, 0 0 3px #ffffff;
  }
</style>
</head>
<body>
  <main class="card">
    <div class="brand-mark"><span class="brand-mark__name">LUMEN</span></div>
    <div class="title-band"></div>
    <h1 class="company-name">LUMEN ACCOUNTING &amp;<br>TAXATION SOLUTIONS</h1>
    <p class="person-name">Corwin Pell</p>
    <p class="role">Accountant / Business Consultant</p>
    <p class="contact">Tel: Tel : (868) 512-4873 /<br>(868) 587-2196</p>
  </main>
</body>
</html>
```